Preparation for STEADFAST HORIZON

Size 8.5 x 11 Front and Back cover.
I need a front cover for a workbook that will be used by couples participating in a program we are calling STEADFAST HORIZONREACH HIGHER REACH TOGETHER

Need a back cover that carries over from front cover design.

I would like the finish size to be 8.5 x 11. Bleeds to edge. Back cover to carry over from front.

Target Market(s)

Couples

Font styles to use
Other font styles liked:
• Similar font to logo downloaded

Colors
33b8a4
00a990
86cfc6

Requirements
Must have
• 1. Wording on the page should be:
• Preparation for
• STEADFAST HORIZON
• REACH HIGHER REACH TOGETHER
• Workbook
• 2. Use downloaded logo for the STEADFAST HORIZON Reach Higher Reach Together
• 3. Someplace on the bottom of the page should have:
• Name ________________________________
• Date _________________________________
• 4. And our logo for HearthWorks USA
Nice to have
• Some pictures in the background of married couples that show diversity of age and race (Hispanic, White and Black),

```html
<!DOCTYPE html>
<html lang="en">
<head>
<meta charset="utf-8">
<title>Preparation for Steadfast Horizon – Workbook Cover</title>
<link href="https://fonts.googleapis.com/css2?family=Montserrat:wght@600;700&family=Questrial&display=swap" rel="stylesheet">
<style>
  :root {
    --teal: #33b8a4;
    --teal-soft: #86cfc6;
    --teal-deep: #00a990;
    --ink: #1f2a2a;
    --photo-light: #e4e4e4;
    --photo-mid: #b9b9b9;
    --photo-dark: #6e6e6e;
  }
  * { margin: 0; padding: 0; box-sizing: border-box; }
  html, body { width: 1200px; height: 927px; overflow: hidden; background: #fff; }
  .cover { position: relative; width: 1200px; height: 927px; overflow: hidden; font-family: "Questrial", sans-serif; color: var(--ink); }

  /* back cover */
  .back-photo-top { position: absolute; left: 0; top: 0; width: 565px; height: 278px;
    background: linear-gradient(135deg, #d9d9d9 0%, #a8a8a8 45%, #5f5f5f 100%); }
  .back-photo-bottom { position: absolute; left: 0; top: 625px; width: 565px; height: 302px;
    background: linear-gradient(160deg, #8d8d8d 0%, #c4c4c4 50%, #4e4e4e 100%); }
  .back-band { position: absolute; left: 0; top: 278px; width: 565px; height: 347px; background: var(--teal-soft); }
  .back-title { position: absolute; left: 0; top: 290px; width: 597px; text-align: center;
    font-size: 32px; line-height: 29px; letter-spacing: 0.5px; }
  .back-copy { position: absolute; left: 80px; top: 352px; width: 436px;
    font-size: 12.6px; line-height: 16.35px; text-align: justify; }

  /* front cover */
  .front-photo { position: absolute; left: 565px; top: 0; width: 635px; height: 927px;
    background: linear-gradient(180deg, #ececec 0%, #d8d8d8 40%, #bdbdbd 65%, #d4d4d4 100%); }

  /* spine */
  .spine-title { position: absolute; left: 610px; top: 152px; transform-origin: 0 0; transform: rotate(90deg);
    font-size: 27px; letter-spacing: 0.6px; white-space: nowrap; }
  .spine-brand { position: absolute; left: 612px; top: 632px; transform-origin: 0 0; transform: rotate(90deg);
    display: flex; align-items: center; gap: 4px; font-size: 9px; white-space: nowrap; color: var(--ink); }
  .brand-mark { width: 10px; height: 10px; background: var(--ink); display: inline-block; }

  .front-kicker { position: absolute; left: 690px; width: 476px; top: 44px; text-align: center;
    font-size: 29px; letter-spacing: 0.5px; }
  .front-title { position: absolute; left: 660px; width: 536px; top: 82px; text-align: center;
    font-family: "Montserrat", sans-serif; font-weight: 600; color: var(--teal-soft);
    font-size: 58px; line-height: 64px; letter-spacing: 1px; }
  .front-tagline { position: absolute; left: 690px; width: 476px; top: 221px; text-align: center;
    font-size: 27px; letter-spacing: 0.3px; }
  .front-label { position: absolute; left: 690px; width: 436px; top: 266px; text-align: center;
    font-family: "Montserrat", sans-serif; font-weight: 700; color: var(--teal-soft); font-size: 25px; }

  .entry-box { position: absolute; left: 689px; top: 707px; width: 481px; height: 101px;
    background: rgba(134, 207, 198, 0.85); padding: 10px 10px 0 10px; }
  .entry-line { font-size: 30px; line-height: 34px; border-bottom: 1px solid rgba(31,42,42,0.5); height: 34px; }

  .front-brand { position: absolute; left: 868px; top: 850px; display: flex; align-items: center; gap: 6px;
    font-size: 13px; color: var(--ink); }
  .front-brand .brand-mark { width: 14px; height: 14px; }
</style>
</head>
<body>
<div class="cover">
  <div class="back-photo-top" role="img" aria-label="Black and white photo of hands exchanging a wedding ring"></div>
  <div class="back-band"></div>
  <div class="back-photo-bottom" role="img" aria-label="Black and white photo of a bride and groom at a candlelit ceremony with guests"></div>

  <h2 class="back-title">STEADFAST<br>HORIZON</h2>
  <p class="back-copy">Lorem ipsum dolor sit amet, consectetur adipisicing elit, sed do eiusmod tempor incididunt ut labore et dolore magna aliqua. Ut enim ad minim veniam, quis nostrud exercitation ullamco laboris nisi ut aliquip ex ea commodo consequat. Duis aute irure dolor in reprehenderit in voluptate velit esse cillum dolore eu fugiat nulla pariatur. Excepteur sint occaecat cupidatat non proident, sunt in culpa qui officia deserunt mollit anim id est laborum. Sed ut perspiciatis unde omnis iste natus error sit voluptatem accusantium doloremque laudantium, totam rem aperiam, eaque ipsa quae ab illo inventore veritatis et quasi architecto beatae vitae dicta sunt explicabo. Nemo enim ipsam voluptatem quia voluptas sit aspernatur aut odit aut fugit, sed quia consequuntur magni dolores eos qui ratione voluptatem sequi nesciunt. Neque porro quisquam est, qui dolorem ipsum quia dolor sit amet, consectetur, adipisci velit, sed quia non</p>

  <div class="front-photo" role="img" aria-label="Black and white photo of a couple seen from behind, holding hands on a beach under a cloudy sky"></div>

  <div class="spine-title">STEADFAST HORIZON</div>
  <div class="spine-brand"><span class="brand-mark"></span>HearthWorks USA</div>

  <div class="front-kicker">PREPARATION FOR</div>
  <h1 class="front-title">STEADFAST<br>HORIZON</h1>
  <div class="front-tagline">REACH HIGHER REACH TOGETHER</div>
  <div class="front-label">Workbook</div>

  <div class="entry-box">
    <div class="entry-line">NAME</div>
    <div class="entry-line">DATE</div>
  </div>

  <div class="front-brand"><span class="brand-mark"></span>HearthWorks USA</div>
</div>
</body>
</html>
```